Investment company needing business card

We are wanting a business card which looks sharp and easy on the eye. We are thinking of having a business card with the logo embossed on it, to really make it stand out. We will only have a small amount of information of the business card, person's name, position, email address and phone number

Contact Information for Business Card

Danica Pruett
Executive Assistant
+64 21 547 3162
danicap@harwellcapital.co.nz

Requirements
Must have
• Embossed logo
Should not have
• Not to be busy

```html
<!DOCTYPE html>
<html lang="en">
<head>
<meta charset="utf-8">
<title>Harwell Capital – Business Card</title>
<link rel="stylesheet" href="https://fonts.googleapis.com/css2?family=Lato:wght@400;700;900&display=swap">
<style>
  :root {
    --bg: #2b2b2d;
    --card-white: #ffffff;
    --card-grey: #6a6b6d;
    --emboss: #3b3c3e;
    --green: #21b573;
    --slate: #5e5f61;
    --text-grey: #6d6e70;
  }
  * { box-sizing: border-box; margin: 0; padding: 0; }
  html, body {
    width: 1200px; height: 880px; overflow: hidden;
    background: var(--bg);
    font-family: "Lato", sans-serif;
  }
  .stage {
    width: 1200px; height: 880px;
    display: flex; flex-direction: column;
    align-items: center; justify-content: center; gap: 48px;
  }
  .card {
    position: relative;
    width: 600px; height: 343px;
    border-radius: 22px;
    overflow: hidden;
  }
  .card--back {
    background: var(--card-grey);
    display: flex; align-items: center; justify-content: center;
  }
  .brand {
    display: flex; align-items: center; gap: 14px;
    font-weight: 900; text-transform: uppercase; letter-spacing: 2px;
  }
  .brand__mark { display: block; }
  .card--back .brand { color: var(--emboss); font-size: 40px; }
  .card--back .brand__mark { width: 46px; height: 46px; background: var(--emboss); }

  .card--front { background: var(--card-white); }
  .card--front .brand {
    position: absolute; left: 40px; top: 48px;
    color: var(--green); font-size: 32px;
  }
  .card--front .brand__mark { width: 36px; height: 36px; background: var(--green); }

  .contact {
    position: absolute; left: 40px; top: 190px;
    color: var(--text-grey);
  }
  .contact__name { color: var(--green); font-weight: 700; font-size: 20px; line-height: 1.1; }
  .contact__role { font-size: 15px; margin-bottom: 14px; }
  .contact__line {
    display: flex; align-items: center; gap: 10px;
    font-size: 15px; line-height: 1.5;
  }
  .contact__icon { width: 14px; height: 14px; flex: none; }
  .band { position: absolute; left: 0; bottom: 0; width: 600px; height: 343px; }
</style>
</head>
<body>
<main class="stage">
  <section class="card card--back" aria-label="Card back">
    <div class="brand"><span class="brand__mark"></span>Harwell Capital</div>
  </section>

  <section class="card card--front" aria-label="Card front">
    <svg class="band" viewBox="0 0 600 343" aria-hidden="true">
      <path d="M0 343 L0 330 L360 330 Q372 330 374 318 L376 298 L600 298 L600 309 L382 309 Q380 322 368 322 L0 322 Z" fill="var(--slate)" />
      <path d="M0 343 L0 336 L370 336 Q382 336 384 322 L386 300 Q388 268 400 266 L600 258 L600 343 Z" fill="var(--green)" />
      <path d="M0 336 L370 336 Q382 336 384 322 L386 300 L378 300 L376 320 Q374 330 362 330 L0 330 Z" fill="var(--card-white)" />
    </svg>

    <div class="brand"><span class="brand__mark"></span>Harwell Capital</div>

    <div class="contact">
      <p class="contact__name">Danica Pruett</p>
      <p class="contact__role">Executive Assistant</p>
      <p class="contact__line">
        <svg class="contact__icon" viewBox="0 0 14 14" aria-hidden="true"><rect x="3" y="1" width="8" height="12" rx="1.5" fill="none" stroke="var(--green)" stroke-width="1.5"/></svg>
        +64 21 547 3162
      </p>
      <p class="contact__line">
        <svg class="contact__icon" viewBox="0 0 14 14" aria-hidden="true"><rect x="1" y="3" width="12" height="8" fill="var(--green)"/><path d="M1 3 L7 8 L13 3" fill="none" stroke="#fff" stroke-width="1.2"/></svg>
        danicap@harwellcapital.co.nz
      </p>
    </div>
  </section>
</main>
</body>
</html>
```